Design a menu for health restaurant

A health food restaurant in Los Angeles is seeking menu design. Our foods are made from scratch using whole ingredients.
Name: Grubb Larder
Address: 1000 E 60th StLos Angeles, CA 90247
Website: www.GrubbLarder.example
We are looking for a clean and simple menu. Brand colors are white/tan, green and orange.

Please see attached excel with menu items and logo. We do not yet have prices.

Colors
f78f20
9bcb3c
ffffff
fff3d1

Requirements
Must have
• Easy to read.
Trifold menu design (front and back).
VEGAN, VEGETARIAN, GLUTEN FREE, CONTAINS NUTS symbols.
Logo.
Nice to have
• Incorporate brand colors, but still be easy to read.
We would like to use the Belco font (attached) if it works. If not we are open to a similar font that is easy to read.

Please see attached images.
We like the images and headers of OPTION 1. Would like something similar in trifold format.
We like the clean fonts of OPTION 2.

```html
<!DOCTYPE html>
<html lang="en">
<head>
<meta charset="utf-8">
<title>Grubb Larder Menu</title>
<link href="https://fonts.googleapis.com/css2?family=Signika:wght@400;500;600&family=Passion+One:wght@400;700&display=swap" rel="stylesheet">
<style>
:root{
  --orange:#f78f20;
  --orange-deep:#f26b2a;
  --green:#9bcb3c;
  --white:#ffffff;
  --cream:#fff3d1;
}
*{box-sizing:border-box;margin:0;padding:0}
html,body{width:1200px;height:934px;overflow:hidden;background:var(--white)}
body{position:relative;font-family:"Signika",sans-serif;color:var(--orange)}
.frame{position:absolute;left:26px;top:29px;width:1147px;height:876px;border:3px solid var(--orange)}
.corner-tab{position:absolute;left:0;top:0;width:230px;height:215px}
.brand{position:absolute;left:42px;top:40px;width:156px;height:156px;border-radius:50%;background:var(--white);border:4px solid var(--orange);display:flex;align-items:center;justify-content:center;text-align:center}
.brand-name{font-family:"Signika",sans-serif;font-weight:600;font-size:21px;line-height:1.1;color:var(--orange)}
.tag{position:absolute;display:flex;align-items:center;gap:6px;color:var(--white);font-size:11px;line-height:15px}
.tag-label{background:var(--orange-deep);padding:2px 16px 2px 6px;clip-path:polygon(0 0,94% 0,100% 50%,94% 100%,0 100%)}
.tag-address{left:222px;top:106px}
.tag-web{left:212px;top:166px;font-weight:500;letter-spacing:.3px}
.tag-icon{width:22px;height:22px;flex:none}
.section{position:absolute;border:1px dotted var(--green);padding:0 18px}
.section-title{position:absolute;top:-17px;left:18px;background:var(--white);padding:0 5px;font-family:"Passion One",sans-serif;font-weight:700;font-size:27px;letter-spacing:2px;color:var(--orange);line-height:30px}
.items{list-style:none}
.item{padding:7px 0 6px;border-bottom:1px dotted var(--green)}
.item:last-child{border-bottom:none}
.item-name{font-size:15px;font-weight:500;line-height:19px;display:flex;align-items:center;gap:5px}
.item-desc{font-size:11px;line-height:16px;margin-top:1px;position:relative}
.price{position:absolute;right:0;top:16px;color:var(--green);font-weight:600;font-size:11px}
.icon{width:16px;height:16px;flex:none}
.breakfast{left:50px;top:248px;width:336px;height:527px;padding-top:20px}
.bowls{left:428px;top:121px;width:343px;height:578px;padding-top:16px}
.wraps{left:809px;top:67px;width:343px;height:259px;padding-top:14px}
.soups{left:809px;top:361px;width:343px;height:241px;padding-top:14px}
.combos{left:809px;top:634px;width:343px;height:202px;padding-top:14px}
.legend{position:absolute;left:50px;top:794px;width:336px;height:83px;background:var(--cream);border:1px dotted var(--green);display:grid;grid-template-columns:auto auto;justify-content:center;column-gap:26px;row-gap:10px;align-content:center}
.legend-item{display:flex;align-items:center;gap:5px;font-weight:600;font-size:12px;letter-spacing:.3px}
</style>
</head>
<body>
<svg width="0" height="0" style="position:absolute" aria-hidden="true">
  <defs>
    <symbol id="i-vegan" viewBox="0 0 20 20">
      <circle cx="10" cy="10" r="9" fill="none" stroke="#9bcb3c" stroke-width="1.6"/>
      <path d="M5 14c0-6 5-9 10-9 0 6-4 10-10 9z" fill="#9bcb3c"/>
      <path d="M6 14l7-7" stroke="#fff" stroke-width="1"/>
    </symbol>
    <symbol id="i-veg" viewBox="0 0 20 20">
      <circle cx="10" cy="10" r="9" fill="none" stroke="#9bcb3c" stroke-width="1.6"/>
      <path d="M5.5 6l4.5 9 5-11" fill="none" stroke="#9bcb3c" stroke-width="2" stroke-linecap="round" stroke-linejoin="round"/>
    </symbol>
    <symbol id="i-gf" viewBox="0 0 20 20">
      <circle cx="10" cy="10" r="9" fill="none" stroke="#f78f20" stroke-width="1.6"/>
      <path d="M7 16l7-11M8 8l2 3M10 6l2 3M6 11l3 1M8 13l3 0" fill="none" stroke="#f78f20" stroke-width="1.5" stroke-linecap="round"/>
    </symbol>
    <symbol id="i-nut" viewBox="0 0 20 20">
      <circle cx="10" cy="10" r="9" fill="none" stroke="#f78f20" stroke-width="1.6"/>
      <path d="M5 8h10c0 5-2 8-5 8S5 13 5 8z" fill="#f78f20"/>
      <path d="M5 8c0-3 2-4 5-4s5 1 5 4z" fill="none" stroke="#f78f20" stroke-width="1.4"/>
    </symbol>
  </defs>
</svg>

<div class="frame"></div>
<svg class="corner-tab" viewBox="0 0 230 215" aria-hidden="true">
  <path d="M0 0H135L190 50C222 80 225 130 205 165 185 198 150 212 118 212 80 212 55 195 35 172L0 135Z" fill="#f78f20"/>
</svg>
<div class="brand"><span class="brand-name">Grubb<br>Larder</span></div>

<div class="tag tag-address">
  <svg class="tag-icon" viewBox="0 0 22 22" aria-hidden="true"><circle cx="11" cy="11" r="10" fill="#9bcb3c"/><circle cx="11" cy="11" r="7.5" fill="#fff"/><path d="M11 17c-3-4-4-5.5-4-7.5a4 4 0 018 0c0 2-1 3.5-4 7.5z" fill="#9bcb3c"/><circle cx="11" cy="9.5" r="1.4" fill="#fff"/></svg>
  <span class="tag-label">2417 W 83rd St<br>Los Angeles, CA 90247</span>
</div>
<div class="tag tag-web">
  <svg class="tag-icon" viewBox="0 0 22 22" aria-hidden="true"><circle cx="11" cy="11" r="10" fill="#9bcb3c"/><circle cx="11" cy="11" r="6" fill="none" stroke="#fff" stroke-width="1.2"/><path d="M5 11h12M11 5v12M7 8h8M7 14h8" stroke="#fff" stroke-width="1"/></svg>
  <span class="tag-label">www.GrubbLarder.example</span>
</div>

<section class="section breakfast">
  <h2 class="section-title">BREAKFAST</h2>
  <ul class="items">
    <li class="item"><h3 class="item-name">Pastries <svg class="icon"><use href="#i-veg"/></svg></h3>
      <p class="item-desc">Croissant (regular, almond, chocolate)<br>Blueberry Muffin<br>Superseed Cookie<span class="price">11.99</span></p></li>
    <li class="item"><h3 class="item-name">Parfait <svg class="icon"><use href="#i-veg"/></svg></h3>
      <p class="item-desc">Fresh strawberries and blueberries on yogurt<br>and muesli and topped with honey drizzle.</p></li>
    <li class="item"><h3 class="item-name">Avocado Super Toast <svg class="icon"><use href="#i-vegan"/></svg></h3>
      <p class="item-desc">Avocado Mash, Tomato, Basil, Ground Flax,<br>Hemp Seed, Chickpeas, and Moringa Powder<br>on Whole Wheat Bread.</p></li>
    <li class="item"><h3 class="item-name">Brunch Burger</h3>
      <p class="item-desc">House seasoned beef burger topped with<br>an over medium egg, red leaf lettuce, tomato,<br>housemade pickles and Larder Sauce on a bun.</p></li>
    <li class="item"><h3 class="item-name">Breakfast Sammy <svg class="icon"><use href="#i-vegan"/></svg></h3>
      <p class="item-desc">Fresh strawberries and blueberries on yogurt<br>and muesli and topped with honey drizzle.</p></li>
    <li class="item"><h3 class="item-name">AM Burrito <svg class="icon"><use href="#i-veg"/></svg></h3>
      <p class="item-desc">Scrambled eggs, onion, red bell pepper,<br>black beans, housemade salsa, yogurt, and peppe<br>jack cheese in a tortilla.</p></li>
  </ul>
</section>

<div class="legend">
  <span class="legend-item"><svg class="icon"><use href="#i-vegan"/></svg>VEGAN</span>
  <span class="legend-item"><svg class="icon"><use href="#i-veg"/></svg>VEGETARIAN</span>
  <span class="legend-item"><svg class="icon"><use href="#i-gf"/></svg>GLUTEN FREE</span>
  <span class="legend-item"><svg class="icon"><use href="#i-nut"/></svg>CONTAINS NUTS</span>
</div>

<section class="section bowls">
  <h2 class="section-title">BOWLS</h2>
  <ul class="items">
    <li class="item"><h3 class="item-name">Southwest Bowl <svg class="icon"><use href="#i-gf"/></svg><svg class="icon"><use href="#i-nut"/></svg></h3>
      <p class="item-desc">Your choice of protein with corn, black beans,<br>red onions, almonds and avocado over quinoa<br>with lime hot sauce.</p></li>
    <li class="item"><h3 class="item-name">Chimi Bowl <svg class="icon"><use href="#i-gf"/></svg></h3>
      <p class="item-desc">Your choice of protein with red bell pepper, mushrooms,<br>zucchini, squash, onion, cherry tomatoes and<br>fresh herb chimichurri on wild and brown rice.</p></li>
    <li class="item"><h3 class="item-name">Soba Noodle Bowl</h3>
      <p class="item-desc">Your choice of protein with spinach, snow peas,<br>roasted carrots, red bell pepper, cilantro, sesame seeds<br>and ginger lime sauce over soba noodles.</p></li>
    <li class="item"><h3 class="item-name">Hollywood Bowl <svg class="icon"><use href="#i-gf"/></svg></h3>
      <p class="item-desc">Your choice of protein with broccoli, roasted corn,<br>cherry tomatoes, basil, pepitas, flax seeds and<br>lemon juice on wild and brown rice.</p></li>
    <li class="item"><h3 class="item-name">Larder Bowl <svg class="icon"><use href="#i-gf"/></svg></h3>
      <p class="item-desc">Your choice of protein with roasted chickpeas and<br>cauliflower, zesty fennel salad and citrus yogurt.</p></li>
    <li class="item"><h3 class="item-name">Buddha Bowl</h3>
      <p class="item-desc">Your choice of protein with corn, red kale, sweet potatoes,<br>red cabbage, parsley, oregano, hummus, and farro.</p></li>
    <li class="item"><h3 class="item-name">Chili Rice Bowl <svg class="icon"><use href="#i-gf"/></svg></h3>
      <p class="item-desc">Chicken, onions, bell peppers, jalapeños, black &amp;<br>kidney beans, and tomato over brown rice.</p></li>
  </ul>
</section>

<section class="section wraps">
  <h2 class="section-title">WRAPS</h2>
  <ul class="items">
    <li class="item"><h3 class="item-name">Rancher's Wrap</h3>
      <p class="item-desc">Tomato, red onion, hard boiled egg, avocado,<br>feta cheese, microgreens, romaine, grilled chicken &amp;<br>Ranch dressing in a grilled wrap.</p></li>
    <li class="item"><h3 class="item-name">Vegan Tuna Wrap <svg class="icon"><use href="#i-vegan"/></svg></h3>
      <p class="item-desc">Vegan tuna, romaine, avocado, celery, shallot, &amp; oregano<br>with Herbalicious Sauce in a whole grain wrap.</p></li>
    <li class="item"><h3 class="item-name">Vegetarian Wrap <svg class="icon"><use href="#i-veg"/></svg></h3>
      <p class="item-desc">Roasted chickpeas, romaine, avocado, red bell pepper,<br>shaved carrots, cucumber, spinach, basil, black beans &amp;<br>feta with lemon-hummus in a sprouted 7-grain wrap.</p></li>
  </ul>
</section>

<section class="section soups">
  <h2 class="section-title">SOUPS</h2>
  <ul class="items">
    <li class="item"><h3 class="item-name">Chicken Noodle <svg class="icon"><use href="#i-gf"/></svg></h3>
      <p class="item-desc">Chicken, egg noodles, root vegetables, oregano &amp;<br>peppercorns.</p></li>
    <li class="item"><h3 class="item-name">Larder Chili <svg class="icon"><use href="#i-gf"/></svg></h3>
      <p class="item-desc">Chicken, onions, bell peppers, jalapeños, black &amp;<br>kidney beans, and tomato.</p></li>
    <li class="item"><h3 class="item-name">Seasonal Rotating <svg class="icon"><use href="#i-vegan"/></svg><svg class="icon"><use href="#i-nut"/></svg></h3>
      <h3 class="item-name">(Butternut Squash Soup</h3>
      <p class="item-desc">Butternut squash blended with warm spices, and<br>coconut milk.</p></li>
  </ul>
</section>

<section class="section combos">
  <h2 class="section-title">COMBOS</h2>
  <ul class="items">
    <li class="item"><h3 class="item-name">Soup + Salad</h3>
      <p class="item-desc">Your choice of soup and side salad.<br>16oz soup + 38oz salad</p></li>
    <li class="item"><h3 class="item-name">Avo Toast Combo</h3>
      <p class="item-desc">Half avocado toast and your choice of soup. 16oz</p></li>
    <li class="item"><h3 class="item-name">Soup + Sammy</h3>
      <p class="item-desc">Your choice of soup and sandwich.<br>16oz soup + Sandwich</p></li>
  </ul>
</section>
</body>
</html>
```